Rancho Miralta - New Community in Seybaplaya
Affordable Country Lots in Campeche, Mexico
Rancho Miralta - New Community in Seybaplaya - Real Estate
Creative Brief
Real Estate
ranchomiralta.example
Not for profit company to promote affordable lots in Canada aiming at attracting soon to be retirees and young investors alike.
Company is family run and simple to operate and would like to portray such image.
New community is located 3kms from the beach in tropical weather year round.
Google images of seybaplaya and campeche to get a feel for local existing community.
We would like to show respect to the existing Spanish colonial architecture and heritage.
Likes, colorful, simple, easy to understand and to follow links to navigate within website, not too complicated to update Dislikes, complex, confusing, too plain or too colorful,
Must use existing logo: http://files.brandpixelhub.example/drafts/view/entry/804213/draft/7761904 Pages must fit in one screen and must be written in simple html coding to perform updates without engaging specialty programmers/designers.

```html
<!DOCTYPE html>
<html lang="en">
<head>
<meta charset="utf-8">
<title>Rancho Miralta – Purchasing</title>
<link rel="stylesheet" href="https://fonts.googleapis.com/css2?family=PT+Sans:wght@400;700&display=swap">
<style>
  :root {
    --teal: #1f7a8c;
    --teal-dark: #0f4c63;
    --band: #0b4a66;
    --band-deep: #063a52;
    --panel: #f3f7f8;
    --panel-edge: #ffffff;
    --text: #3a4a52;
    --field-border: #b9c9cf;
    --white: #ffffff;
    --sky-top: #6f8ea6;
    --sky-glow: #e7c9a4;
    --sea: #4f7d94;
  }
  * { box-sizing: border-box; margin: 0; padding: 0; }
  html, body { width: 1200px; height: 600px; overflow: hidden; }
  body { font-family: "PT Sans", Tahoma, sans-serif; color: var(--text); position: relative; background: var(--band-deep); }

  .scenery {
    position: absolute; left: 0; top: 0; width: 1200px; height: 450px;
    background:
      linear-gradient(180deg, var(--sky-top) 0%, #a3b2bd 30%, var(--sky-glow) 52%, #8fa8b6 60%, var(--sea) 78%, var(--band) 100%);
  }
  .footer-band {
    position: absolute; left: 0; top: 450px; width: 1200px; height: 150px;
    background: linear-gradient(180deg, var(--band) 0%, var(--band-deep) 100%);
  }

  .content-panel {
    position: absolute; left: 259px; top: 19px; width: 677px; height: 401px;
    background: var(--panel); border: 4px solid var(--panel-edge); border-radius: 14px;
    box-shadow: 0 2px 10px rgba(0,0,0,.25);
  }

  .brand {
    position: absolute; left: 267px; top: 5px; width: 172px; height: 172px;
    border-radius: 50%; background: var(--white); border: 8px solid var(--teal);
    display: flex; align-items: center; justify-content: center; text-align: center;
    color: var(--teal); font-weight: 700; font-size: 22px; line-height: 1.1;
  }

  .page-title {
    position: absolute; left: 456px; top: 38px;
    color: var(--teal); font-size: 28px; font-weight: 700; letter-spacing: 1px;
  }
  .page-subtitle {
    position: absolute; left: 456px; top: 78px;
    font-size: 13px; font-weight: 700; color: var(--teal-dark);
  }
  .page-intro {
    position: absolute; left: 456px; top: 102px; width: 430px;
    font-size: 11px; line-height: 1.32;
  }

  .contact-form { position: absolute; left: 456px; top: 218px; width: 283px; }
  .field {
    position: absolute; width: 137px; height: 17px;
    border: 1px solid var(--field-border); background: var(--white);
    font: 10px "PT Sans", Tahoma, sans-serif; color: #8a9aa2; padding: 0 4px;
  }
  .field-name { left: 0; top: 0; }
  .field-phone { left: 146px; top: 0; }
  .field-surname { left: 0; top: 24px; }
  .field-email { left: 146px; top: 24px; }
  .field-comments { left: 0; top: 48px; width: 283px; height: 72px; resize: none; padding: 3px 4px; }
  .submit-button {
    position: absolute; left: 175px; top: 135px; width: 106px; height: 24px;
    background: var(--teal-dark); color: var(--white); border: 2px solid #d7e4e8; border-radius: 8px;
    font: 700 14px "PT Sans", Tahoma, sans-serif; letter-spacing: 1px;
  }

  .main-nav {
    position: absolute; left: 0; top: 455px; width: 1200px;
    display: flex; justify-content: center; gap: 30px; list-style: none;
  }
  .main-nav a { color: var(--white); text-decoration: none; font-size: 17px; position: relative; }
  .main-nav .is-current::after {
    content: ""; position: absolute; left: 50%; top: 28px; margin-left: -6px;
    border-left: 6px solid transparent; border-right: 6px solid transparent; border-bottom: 7px solid var(--white);
  }

  .copyright {
    position: absolute; left: 0; top: 580px; width: 1200px; text-align: center;
    color: var(--white); font-size: 10px;
  }
</style>
</head>
<body>
  <div class="scenery" role="img" aria-label="Photograph of a calm sea at sunset under a cloudy sky"></div>
  <div class="footer-band"></div>

  <main class="content-panel"></main>

  <div class="brand">Rancho<br>Miralta</div>

  <h1 class="page-title">PURCHASING</h1>
  <p class="page-subtitle">The standard Lorem Ipsum passage, used since the 1500s</p>
  <p class="page-intro">"Lorem ipsum dolor sit amet, consectetur adipisicing elit, sed do eiusmod tempor incididunt ut labore et dolore magna aliqua. Ut enim ad minim veniam, quis nostrud exercitation ullamco laboris nisi ut aliquip ex ea commodo consequat. Duis aute irure dolor in reprehenderit in voluptate velit esse cillum dolore eu fugiat nulla pariatur. Excepteur sint occaecat cupidatat non proident, sunt in culpa qui officia deserunt mollit anim id est laborum."</p>

  <form class="contact-form">
    <input class="field field-name" type="text" placeholder="Your Name">
    <input class="field field-phone" type="text" placeholder="Your Telephone">
    <input class="field field-surname" type="text" placeholder="Your Surname">
    <input class="field field-email" type="text" placeholder="Your e-mail">
    <textarea class="field field-comments" placeholder="Comments"></textarea>
    <button class="submit-button" type="button">SUBMIT</button>
  </form>

  <nav>
    <ul class="main-nav">
      <li><a href="#">Home</a></li>
      <li><a href="#">Master Plan</a></li>
      <li><a href="#">Campeche</a></li>
      <li><a href="#">Gallery</a></li>
      <li><a href="#" class="is-current">Purchasing</a></li>
      <li><a href="#">Legal</a></li>
    </ul>
  </nav>

  <p class="copyright">Copyright © Rancho Miralta 2011</p>
</body>
</html>
```